International Trading Company, 'KIRO' needs a Business Card

The company name is "KIRO" and it has own logo design.
I'd like to use its logo on this business card.
I need two side Business Card.
I'll look forward to your great design.
Thank you very much in advance.

Contact Information for Business Card

Company Name : Kiro Harbour Limited
Information Example
Dorian Pallister
Mobile(use icon please) : 1 (212) 555-0143
Tel(use icon please) : 1 (212) 555-0178
Email(use icon please) : dorian27@kiroharbour-mail.com
Address(use icon please) : 482 Halden Ave, New York, NY 10160, USA

```html
<!DOCTYPE html>
<html lang="en">
<head>
<meta charset="utf-8">
<title>Kiro Harbour Limited – Business Card</title>
<link href="https://fonts.googleapis.com/css2?family=Open+Sans:wght@400;600;800&display=swap" rel="stylesheet">
<style>
  :root {
    --backdrop: #e4e2de;
    --card-stock: #efede8;
    --card-edge: #e0693a;
    --ink: #262626;
    --ink-soft: #4a4a4a;
    --rule: #2d2d2d;
  }
  * { box-sizing: border-box; margin: 0; padding: 0; }
  html, body {
    width: 1200px; height: 918px; overflow: hidden;
    background: var(--backdrop);
    font-family: "Open Sans", Arial, sans-serif;
    color: var(--ink);
  }
  .sheet {
    width: 1200px; height: 918px;
    display: flex; flex-direction: column;
    align-items: center; justify-content: center; gap: 64px;
  }
  .card {
    width: 620px; height: 354px;
    background: var(--card-stock);
    border-bottom: 4px solid var(--card-edge);
    box-shadow: 0 10px 28px rgba(0,0,0,.14);
    position: relative;
  }

  /* Front */
  .card--front {
    display: flex; align-items: center; justify-content: center;
  }
  .lockup { text-align: center; color: var(--ink); font-weight: 800; }
  .lockup__name {
    font-size: 118px; line-height: .9; letter-spacing: 2px;
  }
  .lockup__company {
    font-size: 27px; letter-spacing: 7px; text-transform: uppercase;
    margin-top: 10px;
  }

  /* Back */
  .card--back {
    display: grid; grid-template-columns: 272px 1px 1fr;
    align-items: center; padding: 0 34px 0 36px;
  }
  .card--back .lockup__name { font-size: 64px; }
  .card--back .lockup__company { font-size: 14px; letter-spacing: 3.5px; margin-top: 6px; }
  .divider { width: 1px; height: 176px; background: var(--rule); }
  .details { padding-left: 26px; }
  .person { text-align: right; margin-bottom: 24px; }
  .person__name { font-size: 22px; font-weight: 400; }
  .person__role { font-size: 10px; font-weight: 600; color: var(--ink-soft); letter-spacing: .5px; }
  .contacts { list-style: none; }
  .contact {
    display: flex; align-items: center; gap: 10px;
    font-size: 11.5px; color: var(--ink-soft);
    margin-bottom: 9px;
  }
  .contact__icon {
    width: 17px; height: 17px; flex: none;
    border: 1.3px solid var(--ink); border-radius: 3px;
    display: flex; align-items: center; justify-content: center;
  }
  .contact__icon svg { width: 11px; height: 11px; fill: var(--ink); }
</style>
</head>
<body>
<main class="sheet">
  <section class="card card--front" aria-label="Business card front">
    <div class="lockup">
      <div class="lockup__name">KIRO</div>
      <div class="lockup__company">Kiro Harbour Limited</div>
    </div>
  </section>

  <section class="card card--back" aria-label="Business card back">
    <div class="lockup">
      <div class="lockup__name">KIRO</div>
      <div class="lockup__company">Kiro Harbour Limited</div>
    </div>
    <div class="divider"></div>
    <div class="details">
      <div class="person">
        <div class="person__name">Dorian Pallister</div>
        <div class="person__role">Managing Director</div>
      </div>
      <ul class="contacts">
        <li class="contact">
          <span class="contact__icon"><svg viewBox="0 0 12 12" aria-hidden="true"><path d="M6 0.5a3.8 3.8 0 0 0-3.8 3.8C2.2 7.2 6 11.5 6 11.5s3.8-4.3 3.8-7.2A3.8 3.8 0 0 0 6 .5zm0 5.3a1.5 1.5 0 1 1 0-3 1.5 1.5 0 0 1 0 3z"/></svg></span>
          482 Halden Ave, New York, NY 10160, USA
        </li>
        <li class="contact">
          <span class="contact__icon"><svg viewBox="0 0 12 12" aria-hidden="true"><path d="M1 2.5h10v7H1zM1.6 3.1 6 6.4l4.4-3.3v.9L6 7.3 1.6 4z" fill-rule="evenodd"/></svg></span>
          dorian27@kiroharbour-mail.com
        </li>
        <li class="contact">
          <span class="contact__icon"><svg viewBox="0 0 12 12" aria-hidden="true"><path d="M3.5.5h5a.8.8 0 0 1 .8.8v9.4a.8.8 0 0 1-.8.8h-5a.8.8 0 0 1-.8-.8V1.3a.8.8 0 0 1 .8-.8zM3.7 1.8v7.4h4.6V1.8zM6 9.6a.6.6 0 1 0 0 1.2.6.6 0 0 0 0-1.2z" fill-rule="evenodd"/></svg></span>
          1 (212) 555-0143
        </li>
        <li class="contact">
          <span class="contact__icon"><svg viewBox="0 0 12 12" aria-hidden="true"><path d="M2.6.8 4.4 3c.3.3.2.7 0 1L3.6 5c.7 1.4 1.9 2.6 3.3 3.3l1-.8c.3-.3.7-.3 1 0l2.2 1.8c.3.3.3.7 0 1l-1 1c-.5.4-1.2.5-1.8.2C5.4 10.3 1.7 6.6.5 3.7.2 3.1.3 2.4.8 1.9l.8-1c.3-.3.7-.3 1-.1z"/></svg></span>
          1 (212) 555-0178
        </li>
      </ul>
    </div>
  </section>
</main>
</body>
</html>
```